Business Card Design - Cryotherapy

We need a custom created business card for our company FrostLeaf Spa. We provide whole body cryotherapy and localized cryotherapy to our clients. Please be creative.
Please see our website for idea's on design.
www.frostleafspa-example.com
Industry/Entity Type
Business
Contact Information for Business Card
Name, Position, Phone Number, Address, Website, Email
Look and feel
Each slider illustrates characteristics of the customer's brand and the style your logo design should communicate.

```html
<!DOCTYPE html>
<html lang="en">
<head>
<meta charset="utf-8">
<title>FrostLeaf Spa – Business Card</title>
<link rel="stylesheet" href="https://fonts.googleapis.com/css2?family=Open+Sans:wght@400;600;700&display=swap">
<style>
  :root {
    --page-bg: #e9e6e1;
    --card-white: #fbfbfb;
    --teal: #17a693;
    --teal-dark: #0b8c86;
    --teal-light: #1cbb9c;
    --ink: #3d3d3d;
    --ink-soft: #6a6a6a;
    --rule: #8fd3c6;
  }
  * { box-sizing: border-box; margin: 0; padding: 0; }
  html, body { width: 1200px; height: 780px; overflow: hidden; }
  body {
    background: var(--page-bg);
    font-family: "Open Sans", Arial, sans-serif;
    display: flex;
    align-items: center;
    justify-content: center;
    gap: 60px;
  }
  .card {
    width: 525px;
    height: 300px;
    border-radius: 16px;
    box-shadow: 0 10px 30px rgba(0,0,0,0.18);
    position: relative;
    overflow: hidden;
  }

  /* Front */
  .card-front {
    background: var(--card-white);
    display: flex;
  }
  .brand-block {
    width: 215px;
    display: flex;
    flex-direction: column;
    align-items: center;
    justify-content: center;
    gap: 18px;
  }
  .brand-dot {
    width: 92px;
    height: 92px;
    border-radius: 50%;
    background: linear-gradient(135deg, var(--teal-light), var(--teal-dark));
  }
  .brand-name {
    font-weight: 600;
    font-size: 21px;
    color: var(--teal);
    letter-spacing: 0.5px;
  }
  .divider {
    width: 1px;
    margin: 60px 0;
    background: var(--rule);
  }
  .contact-block {
    flex: 1;
    padding: 52px 0 0 30px;
    color: var(--ink);
  }
  .person-name {
    font-weight: 700;
    font-size: 22px;
    color: var(--teal);
    line-height: 1.1;
  }
  .person-title {
    font-size: 13px;
    color: var(--ink-soft);
    margin-bottom: 40px;
  }
  .address {
    font-size: 12px;
    line-height: 1.45;
    margin-bottom: 8px;
  }
  .contact-list { list-style: none; font-size: 12px; line-height: 1.55; }
  .contact-list li { display: flex; align-items: center; gap: 7px; }
  .icon {
    width: 13px; height: 13px;
    border-radius: 2px;
    background: var(--teal);
    display: inline-flex;
    align-items: center;
    justify-content: center;
  }
  .icon svg { width: 9px; height: 9px; }

  /* Back */
  .card-back {
    background: radial-gradient(ellipse at 45% 40%, var(--teal-light) 0%, var(--teal) 45%, var(--teal-dark) 100%);
    display: flex;
    align-items: center;
    justify-content: center;
    gap: 20px;
  }
  .back-dot {
    width: 70px;
    height: 70px;
    border-radius: 50%;
    background: rgba(255,255,255,0.85);
  }
  .back-name {
    font-weight: 600;
    font-size: 40px;
    color: #ffffff;
    letter-spacing: 1px;
  }
</style>
</head>
<body>
  <section class="card card-front" aria-label="Business card front">
    <div class="brand-block">
      <div class="brand-dot"></div>
      <div class="brand-name">FrostLeaf Spa</div>
    </div>
    <div class="divider"></div>
    <div class="contact-block">
      <div class="person-name">Employee Name</div>
      <div class="person-title">Director</div>
      <p class="address">482 Willow Crest Avenue, Suite 210<br>Lakeview Park, IL 60099</p>
      <ul class="contact-list">
        <li><span class="icon"><svg viewBox="0 0 10 10"><path d="M2 1 L4 1 L4.6 3 L3.5 3.8 Q4.5 5.8 6.2 6.5 L7 5.4 L9 6 L9 8 Q5 9 2.5 6 Q1 4 2 1Z" fill="#fff"/></svg></span>(555) 014-2273</li>
        <li><span class="icon"><svg viewBox="0 0 10 10"><rect x="1" y="2.5" width="8" height="5.5" fill="none" stroke="#fff" stroke-width="1"/><path d="M1 2.5 L5 5.5 L9 2.5" fill="none" stroke="#fff" stroke-width="1"/></svg></span>info@frostleafspa-example.com</li>
        <li><span class="icon"><svg viewBox="0 0 10 10"><circle cx="5" cy="5" r="3.8" fill="none" stroke="#fff" stroke-width="1"/><path d="M1.2 5 H8.8 M5 1.2 V8.8" stroke="#fff" stroke-width="0.8"/></svg></span>www.frostleafspa-example.com</li>
      </ul>
    </div>
  </section>

  <section class="card card-back" aria-label="Business card back">
    <div class="back-dot"></div>
    <div class="back-name">FrostLeaf Spa</div>
  </section>
</body>
</html>
```